Seeking for catalogue design -for Event Mgmt company

Need to be creative and striking and images to be more enhanced.
The items in the catalogue have to be layout well and easy to read.
Cover and background of catalogue needs to be striking but not overpowering the items.
Catologue needs to be able to put up on website and able to read on mobile.
Font used must be easily readable and not too small.

Target Market(s)

Business and Public Sectors

Industry/Entity Type

Event Planning

Colors

Designer to choose colors to be used in the design.

Requirements
Must have
• Not too many colors but must be creative
Nice to have
• See that the images of items in catalogue have better layout
Should not have
• Not to be so messy

```html
<!DOCTYPE html>
<html lang="en">
<head>
<meta charset="utf-8">
<title>Carnival Game Stalls – Lancefield Events</title>
<link rel="stylesheet" href="https://fonts.googleapis.com/css2?family=Open+Sans:wght@700&family=Ubuntu:wght@400;500&display=swap">
<style>
  :root{
    --paper:#ffffff;
    --teal-pale:#b4e8e4;
    --teal-light:#97dcdb;
    --teal-mid:#80ccd3;
    --teal-deep:#6fbfc8;
    --ink:#3a3a3a;
    --ink-soft:#2f3a3d;
    --frame:#9a9a9a;
    --logo-bg:#8d8886;
    --white:#ffffff;
  }
  *{box-sizing:border-box;margin:0;padding:0}
  html,body{width:848px;height:1200px;overflow:hidden;background:var(--paper)}
  .page{position:relative;width:848px;height:1200px;overflow:hidden;background:var(--paper);font-family:"Ubuntu",sans-serif;color:var(--ink-soft)}
  .backdrop{position:absolute;inset:0;width:848px;height:1200px}
  .brand{position:absolute;left:0;top:0;width:198px;height:64px;background:var(--logo-bg);display:flex;align-items:center;justify-content:center}
  .brand-name{font-family:"Ubuntu",sans-serif;font-weight:400;font-size:27px;letter-spacing:1px;color:var(--white);text-transform:uppercase}
  .page-number{position:absolute;right:12px;top:0;font-family:"Ubuntu",sans-serif;font-weight:500;font-size:36px;color:var(--white);line-height:44px}
  .stall{position:absolute;width:290px;text-align:center}
  .stall-heading{font-family:"Open Sans",sans-serif;font-weight:700;font-size:15.5px;color:var(--ink);letter-spacing:.2px;line-height:20px}
  .stall-photo{display:block;width:140px;height:188px;margin:7px auto 0;border:3px solid var(--frame);box-shadow:2px 3px 4px rgba(0,0,0,.18)}
  .stall-info{margin-top:13px;font-size:16.5px;line-height:20.6px;letter-spacing:.3px;color:var(--ink-soft)}
  .terms{position:absolute;left:0;right:0;top:1118px;border-top:1px solid #4a4a4a;padding:8px 0 0 26px;font-size:14.2px;line-height:18.5px;letter-spacing:.3px;font-weight:500;color:var(--ink-soft)}
</style>
</head>
<body>
<div class="page">
  <svg class="backdrop" viewBox="0 0 848 1200" aria-hidden="true">
    <path d="M0 370 C180 300 420 300 560 420 C690 530 770 720 848 860 L848 1200 L0 1200 Z" fill="var(--teal-pale)"/>
    <path d="M0 560 C160 470 380 440 560 520 C700 590 800 720 848 790 L848 1200 L0 1200 Z" fill="var(--teal-light)"/>
    <path d="M0 760 C200 560 480 470 660 560 C780 620 848 700 848 700 L848 1200 L0 1200 Z" fill="var(--teal-mid)"/>
    <path d="M640 1200 C700 1050 760 900 848 820 L848 1200 Z" fill="var(--paper)" opacity=".55"/>
    <path d="M548 0 C548 120 640 210 760 250 C800 262 830 300 848 325 L848 0 Z" fill="var(--teal-pale)"/>
    <path d="M610 0 C610 110 690 190 790 215 C815 222 835 230 848 240 L848 0 Z" fill="var(--teal-deep)"/>
  </svg>

  <div class="brand"><span class="brand-name">Lancefield</span></div>
  <div class="page-number">01</div>

  <section class="stall" style="left:-23px;top:70px">
    <h2 class="stall-heading">CARNIVAL GAME STALLS</h2>
    <svg class="stall-photo" role="img" aria-label="Ring toss game booth with carnival backdrop and pegs"><rect width="100%" height="100%" fill="#d9e8ec"/><rect y="55%" width="100%" height="45%" fill="#2b2f3c"/><rect y="45%" width="100%" height="10%" fill="#e46a6a"/></svg>
    <p class="stall-info">Carnival Ring Toss<br>0.93m by 0.93m<br>$145/stall (Min 3 stalls)<br>Require 1x Table<br>Subsequent day: $70</p>
  </section>
  <section class="stall" style="left:279px;top:70px">
    <h2 class="stall-heading">CARNIVAL GAME STALLS</h2>
    <svg class="stall-photo" role="img" aria-label="Milk cans toss game booth with stacked cans"><rect width="100%" height="100%" fill="#eef2f5"/><rect y="70%" width="100%" height="30%" fill="#cfe3ea"/></svg>
    <p class="stall-info">Milk Cans Toss<br>0.93m by 0.93m<br>$145/stall (Min 3 stalls)<br>Require 1x Table<br>Subsequent day: $70</p>
  </section>
  <section class="stall" style="left:582px;top:70px">
    <h2 class="stall-heading">CARNIVAL GAME STALLS</h2>
    <svg class="stall-photo" role="img" aria-label="Match the colour game booth with coloured grid"><rect width="100%" height="100%" fill="#2a2430"/><rect y="50%" width="100%" height="50%" fill="#a8463f"/></svg>
    <p class="stall-info">Match The Colour<br>0.93m by 0.93m<br>$145/stall (Min 3 stalls)<br>Require 1x Table<br>Subsequent day: $70</p>
  </section>

  <section class="stall" style="left:-20px;top:424px">
    <h2 class="stall-heading">CARNIVAL GAME STALLS</h2>
    <svg class="stall-photo" role="img" aria-label="Feed the clown bean bag game booth"><rect width="100%" height="100%" fill="#f1c58a"/><rect y="65%" width="100%" height="35%" fill="#f4eeee"/></svg>
    <p class="stall-info">Feed The Clown<br>0.93m by 0.93m<br>$145/stall (Min 3 stalls)<br>Require 1x Table<br>Subsequent day: $70</p>
  </section>
  <section class="stall" style="left:279px;top:424px">
    <h2 class="stall-heading">CARNIVAL GAME STALLS</h2>
    <svg class="stall-photo" role="img" aria-label="Feed the bear bean bag game booth with brick backdrop"><rect width="100%" height="100%" fill="#c29a6a"/><rect y="68%" width="100%" height="32%" fill="#d97a5c"/></svg>
    <p class="stall-info">Feed The Bear<br>0.93m by 0.93m<br>$145/stall (Min 3 stalls)<br>Require 1x Table<br>Subsequent day: $70</p>
  </section>
  <section class="stall" style="left:582px;top:424px">
    <h2 class="stall-heading">CARNIVAL GAME STALLS</h2>
    <svg class="stall-photo" role="img" aria-label="Feed the pig bean bag game booth"><rect width="100%" height="100%" fill="#8fd07a"/><rect y="15%" width="100%" height="50%" fill="#eea3a8"/><rect y="65%" width="100%" height="35%" fill="#d9c79a"/></svg>
    <p class="stall-info">Feed The Pig<br>0.93m by 0.93m<br>$145/stall (Min 3 stalls)<br>Require 1x Table<br>Subsequent day: $70</p>
  </section>

  <section class="stall" style="left:-21px;top:777px">
    <h2 class="stall-heading">CARNIVAL GAME STALLS</h2>
    <svg class="stall-photo" role="img" aria-label="Shoot the duck target game booth with toy blaster"><rect width="100%" height="100%" fill="#5fa3c8"/><rect y="62%" width="100%" height="8%" fill="#4caa3c"/><rect y="70%" width="100%" height="30%" fill="#bfe6f2"/></svg>
    <p class="stall-info">Shoot The Duck<br>0.93m by 0.93m<br>$145/stall (Min 3 stalls)<br>Require 1x Table<br>Subsequent day: $70</p>
  </section>
  <section class="stall" style="left:283px;top:776px">
    <h2 class="stall-heading">CARNIVAL GAME STALLS</h2>
    <svg class="stall-photo" role="img" aria-label="Shoot the alien target game booth with toy blaster"><rect width="100%" height="100%" fill="#3e5570"/><rect y="48%" width="100%" height="18%" fill="#9a7a54"/><rect y="68%" width="100%" height="32%" fill="#3e5d9a"/></svg>
    <p class="stall-info">Shoot The Alien<br>0.93m by 0.93m<br>$145/stall (Min 3 stalls)<br>Require 1x Table<br>Subsequent day: $70</p>
  </section>
  <section class="stall" style="left:582px;top:777px">
    <h2 class="stall-heading">CARNIVAL GAME STALLS</h2>
    <svg class="stall-photo" role="img" aria-label="Shoot the target game booth with toy blaster"><rect width="100%" height="100%" fill="#aebfc9"/><rect y="40%" width="100%" height="28%" fill="#6d8a4a"/><rect y="70%" width="100%" height="30%" fill="#e6f3f7"/></svg>
    <p class="stall-info">Shoot The Target<br>0.93m by 0.93m<br>$145/stall (Min 3 stalls)<br>Require 1x Table<br>Subsequent day: $70</p>
  </section>

  <footer class="terms">
    <p>*Size stated above is estimated only.</p>
    <p>*Rates include Delivery, Set up, Dismantle and Collection of the equipments.</p>
    <p>*The more items or more days rented, we may be able to quote a much better discounted package rate</p>
  </footer>
</div>
</body>
</html>
```